Graphic lion print design with text

I like the gold effects in image 2 as described in my attached document, but i'm open to other suggestions. The desired image is image 1. This is a gift for a Leo friend. This is going to be printed and framed to be hung on the wall in a large frame, in landscape format. I like the idea of using different font styles to separate the statements.

• I’m open to the suggestions about the font styles, but I want to separate the statements by using different font styles as shown in attached document.
Must be landscape format.
Small fonts preferred, as shown in the attached image.
• I like the gold effect in image 2 but other suggestions/colours welcome
• Please don't stretch the picture so I can have a good resolution. Place the text on another black background template and then paste the picture beside to the text.

```html
<!DOCTYPE html>
<html lang="en">
<head>
<meta charset="UTF-8">
<title>More Than a Conqueror – Lion Print</title>
<link rel="stylesheet" href="https://fonts.googleapis.com/css2?family=Shojumaru&family=Merienda:wght@500&family=Abel&family=Mr+Dafoe&display=swap">
<style>
  :root {
    --bg: #171618;
    --text: #ffffff;
    --gold-light: #f3c15c;
    --gold: #d79d3b;
    --gold-deep: #7a5320;
    --gold-shadow: #2a2015;
  }
  html, body {
    margin: 0;
    padding: 0;
    overflow: hidden;
    background: var(--bg);
  }
  .print {
    position: relative;
    width: 1200px;
    height: 685px;
    background: var(--bg);
    color: var(--text);
    overflow: hidden;
  }
  .lion-art {
    position: absolute;
    left: 700px;
    top: 0;
    width: 500px;
    height: 655px;
    background:
      radial-gradient(ellipse 55% 50% at 62% 45%, var(--gold-light) 0%, var(--gold) 35%, var(--gold-deep) 65%, transparent 85%),
      radial-gradient(ellipse 40% 30% at 90% 10%, rgba(215,157,59,0.5) 0%, transparent 70%);
  }
  .headline {
    position: absolute;
    left: 37px;
    top: 28px;
    margin: 0;
    font-family: "Shojumaru", cursive;
    font-weight: 400;
    font-size: 25px;
    letter-spacing: 0.5px;
    white-space: nowrap;
  }
  .promise {
    position: absolute;
    left: 0;
    width: 945px;
    margin: 0;
    text-align: center;
    font-family: "Abel", sans-serif;
    font-size: 27px;
  }
  .promise--first { top: 81px; }
  .promise--second { top: 122px; }
  .blessing {
    position: absolute;
    left: 37px;
    top: 166px;
    margin: 0;
    font-family: "Merienda", cursive;
    font-weight: 500;
    font-size: 25px;
    line-height: 37.8px;
  }
  .assurance {
    position: absolute;
    left: 470px;
    width: 712px;
    top: 546px;
    margin: 0;
    text-align: center;
    font-family: "Abel", sans-serif;
    font-size: 31px;
    line-height: 40px;
  }
  .amen {
    position: absolute;
    left: 790px;
    top: 624px;
    margin: 0;
    font-family: "Mr Dafoe", cursive;
    font-size: 34px;
    line-height: 1;
  }
</style>
</head>
<body>
<main class="print">
  <div class="lion-art" role="img" aria-label="Golden illustration of a roaring lion in profile, its mane dissolving into gold particles"></div>

  <h1 class="headline">IT DOESN'T MATTER WHO OR WHAT MAY COME AGAINST YOU.</h1>
  <p class="promise promise--first">FOR GOD IS WITH YOU.</p>
  <p class="promise promise--second">HE has made you more than a conqueror.</p>

  <p class="blessing">
    Almighty God<br>
    will come<br>
    through for you<br>
    when you seek<br>
    Him in your moments<br>
    of trouble and unrest.<br>
    May God<br>
    calm the restlessness of your mind<br>
    And still the thoughts that<br>
    worry you.<br>
    Doors will open for<br>
    you, in the most<br>
    unlikeliest of places.
  </p>

  <p class="assurance">
    When you go through deep waters, He will be with you.<br>
    Never will He leave you, Never will He forsake you.
  </p>
  <p class="amen">Amen</p>
</main>
</body>
</html>
```